Meridian Handsets business card design

I would like to see some designs for a business card for Meridian Handsets. I would like the business card to be double sided. It will need to have a similar colour / look and feel to our website www.meridianhandsets.com.au I have also attached our latest flyer. Final designs to be handed over in Photoshop format so that I can edit the business card when needed please.

Industry/Entity Type

Business

Contact Information for Business Card

Gavin Thornley
sales@meridianhandsets.com.au
Business Development Manager
ph: (08) 6197 5821
www.meridianhandsets.com.au

Font styles to use
Serif
Sans Serif

Requirements
Must have
• If you could please utilise our colour scheme as seen on our website and the attached flyer.
• I would also like the final design to be in a Photoshop format so that I can edit it when needed please.

```html
<!DOCTYPE html>
<html lang="en">
<head>
<meta charset="utf-8">
<title>Meridian Handsets — Business Card</title>
<link rel="stylesheet" href="https://fonts.googleapis.com/css2?family=Open+Sans:wght@400;600&family=Roboto:wght@400;700&display=swap">
<style>
  :root {
    --page-bg: #3a3a3c;
    --card-top: #4b5664;
    --card-mid: #26303c;
    --card-bottom: #0c131c;
    --glow: rgba(255,255,255,0.06);
    --text-light: #ffffff;
    --text-soft: #dfe4ea;
    --divider: rgba(255,255,255,0.35);
    --band-blue-start: #0d4fa6;
    --band-blue-end: #1b8fd8;
    --band-green: #2f9a6a;
  }
  * { margin: 0; padding: 0; box-sizing: border-box; }
  html, body { width: 1200px; height: 852px; overflow: hidden; }
  body {
    background: var(--page-bg);
    display: flex;
    flex-direction: column;
    align-items: center;
    justify-content: center;
    gap: 40px;
    font-family: "Open Sans", sans-serif;
  }
  .card {
    position: relative;
    width: 620px;
    height: 354px;
    border-radius: 22px;
    overflow: hidden;
    background: linear-gradient(180deg, var(--card-top) 0%, var(--card-mid) 45%, var(--card-bottom) 100%);
    color: var(--text-light);
  }
  .card-glow {
    position: absolute;
    width: 300px; height: 300px;
    border-radius: 50%;
    background: radial-gradient(circle, var(--glow) 0%, rgba(255,255,255,0) 70%);
    pointer-events: none;
  }
  .card-front .card-glow { left: 250px; top: 10px; }
  .card-back .card-glow { left: 360px; top: -20px; }
  /* Front */
  .card-front .brand {
    position: absolute;
    left: 0; right: 0; top: 128px;
    text-align: center;
  }
  .brand-name {
    font-family: "Open Sans", sans-serif;
    font-weight: 600;
    font-size: 44px;
    letter-spacing: -0.5px;
    line-height: 1;
    color: var(--text-light);
  }
  .brand-tagline {
    font-family: "Open Sans", sans-serif;
    font-size: 19px;
    margin-top: 6px;
    color: var(--text-soft);
  }
  /* Back */
  .card-back .brand {
    position: absolute;
    left: 48px; top: 128px;
    width: 200px;
  }
  .card-back .brand-name {
    font-size: 38px;
    line-height: 1.1;
  }
  .divider {
    position: absolute;
    left: 270px; top: 40px;
    width: 1px; height: 150px;
    background: var(--divider);
    transform: rotate(-4deg);
  }
  .contact {
    position: absolute;
    left: 300px; top: 46px;
    font-family: "Roboto", sans-serif;
  }
  .contact-name { font-weight: 700; font-size: 22px; }
  .contact-title { font-size: 12px; color: var(--text-soft); margin: 2px 0 12px 12px; }
  .contact-list { list-style: none; margin-left: 12px; }
  .contact-list li {
    display: flex; align-items: center; gap: 10px;
    font-size: 13.5px; line-height: 21px; color: var(--text-soft);
  }
  .contact-list svg { width: 12px; height: 12px; fill: var(--text-soft); flex: none; }
  .bands { position: absolute; left: 0; bottom: 0; width: 620px; height: 80px; }
  .band-tagline {
    position: absolute;
    left: 352px; right: 8px; bottom: 0;
    height: 58px;
    display: flex; align-items: center; justify-content: center;
    font-size: 15px;
    color: var(--text-light);
  }
</style>
</head>
<body>
  <section class="card card-front" aria-label="Card front">
    <div class="card-glow"></div>
    <div class="brand">
      <div class="brand-name">Meridian Handsets</div>
      <div class="brand-tagline">Phone systems for your business</div>
    </div>
  </section>

  <section class="card card-back" aria-label="Card back">
    <div class="card-glow"></div>
    <div class="brand">
      <div class="brand-name">Meridian<br>Handsets</div>
    </div>
    <div class="divider"></div>
    <div class="contact">
      <div class="contact-name">Gavin Thornley</div>
      <div class="contact-title">Business Development Manager</div>
      <ul class="contact-list">
        <li><svg viewBox="0 0 24 24"><path d="M6.6 10.8a15 15 0 0 0 6.6 6.6l2.2-2.2c.3-.3.7-.4 1-.2 1.1.4 2.3.6 3.6.6.6 0 1 .4 1 1V20c0 .6-.4 1-1 1A17 17 0 0 1 3 4c0-.6.4-1 1-1h3.5c.6 0 1 .4 1 1 0 1.3.2 2.5.6 3.6.1.3 0 .7-.2 1z"/></svg>(08) 6197 5821</li>
        <li><svg viewBox="0 0 24 24"><path d="M2 5h20v14H2z M4 7v.4l8 5 8-5V7l-8 5z" fill-rule="evenodd"/></svg>sales@meridianhandsets.com.au</li>
        <li><svg viewBox="0 0 24 24"><path d="M12 2a10 10 0 1 0 0 20 10 10 0 0 0 0-20zm0 2c.9 1 1.7 2.7 2 5h-4c.3-2.3 1.1-4 2-5zM4.3 11h3.7c0 .7 0 1.4.1 2H4.3a8 8 0 0 1 0-2zm5.7 0h4a16 16 0 0 1 0 2h-4a16 16 0 0 1 0-2zm6 0h3.7a8 8 0 0 1 0 2H16c.1-.6.1-1.3 0-2zM10 15h4c-.3 2.3-1.1 4-2 5-.9-1-1.7-2.7-2-5z"/></svg>www.meridianhandsets.com.au</li>
      </ul>
    </div>
    <svg class="bands" viewBox="0 0 620 80" aria-hidden="true">
      <defs>
        <linearGradient id="band-blue" x1="0" x2="1" y1="0" y2="0">
          <stop offset="0" stop-color="#0d4fa6"/>
          <stop offset="1" stop-color="#1b8fd8"/>
        </linearGradient>
      </defs>
      <polygon points="0,68 350,68 354,80 0,80" fill="#2f9a6a"/>
      <polygon points="354,80 332,22 620,22 620,80" fill="url(#band-blue)"/>
    </svg>
    <div class="band-tagline">Phone systems for your business</div>
  </section>
</body>
</html>
```